PL Dunmore Electric Yard Sign

Looking to have a yard sign designed that we can place at projects we are working on. Most likely will be 18" H x 24" W but flexible that we can increase the size if necessary. It should include our logo, our phone # 555-214-7796, website pldunmoreelectric.example and slogan, built on integrity, driven by excellence. Colors should match our brand.

```html
<!DOCTYPE html>
<html lang="en">
<head>
<meta charset="utf-8">
<title>PL Dunmore Electric – Yard Sign</title>
<link href="https://fonts.googleapis.com/css2?family=Krona+One&family=Barlow+Condensed:ital,wght@1,600&display=swap" rel="stylesheet">
<style>
  :root {
    --navy: #0f3358;
    --red: #e0202a;
    --white: #ffffff;
    --backdrop: #4a4a4a;
  }
  html, body {
    margin: 0;
    padding: 0;
    width: 1200px;
    height: 1001px;
    overflow: hidden;
    background: var(--backdrop);
  }
  .yard-sign {
    position: absolute;
    left: 120px;
    top: 140px;
    width: 960px;
    height: 720px;
    display: block;
    box-shadow: 0 12px 30px rgba(0,0,0,0.35);
  }
  .brand-name {
    font-family: "Krona One", sans-serif;
    fill: var(--red);
  }
  .phone-number {
    font-family: "Krona One", sans-serif;
    fill: var(--navy);
  }
  .website {
    font-family: "Krona One", sans-serif;
    fill: var(--navy);
  }
  .slogan {
    font-family: "Barlow Condensed", sans-serif;
    font-style: italic;
    font-weight: 600;
    fill: var(--white);
  }
</style>
</head>
<body>
<svg class="yard-sign" viewBox="0 0 960 720" xmlns="http://www.w3.org/2000/svg" aria-label="PL Dunmore Electric yard sign">
  <!-- sign face -->
  <rect class="sign-face" x="0" y="0" width="960" height="720" fill="var(--white)"/>

  <!-- brand name with plain mark -->
  <g class="brand">
    <circle cx="480" cy="110" r="34" fill="var(--red)"/>
    <text class="brand-name" x="480" y="212" font-size="44" text-anchor="middle" textLength="600" lengthAdjust="spacingAndGlyphs">PL Dunmore Electric</text>
  </g>

  <!-- phone -->
  <g class="contact-phone">
    <path d="M92 346 q-6 0 -8 8 q-2 14 10 26 q12 12 26 10 q8 -2 8 -8 l-7 -7 q-4 -3 -8 0 l-3 3 q-8 -3 -14 -14 l3 -3 q3 -4 0 -8 z" fill="var(--red)"/>
    <text class="phone-number" x="130" y="392" font-size="66" textLength="770" lengthAdjust="spacingAndGlyphs">555-214-7796</text>
  </g>

  <!-- website -->
  <g class="contact-web">
    <g fill="none" stroke="var(--red)" stroke-width="3">
      <circle cx="92" cy="451" r="13"/>
      <ellipse cx="92" cy="451" rx="5.5" ry="13"/>
      <line x1="79" y1="451" x2="105" y2="451"/>
      <line x1="82" y1="444" x2="102" y2="444"/>
      <line x1="82" y1="458" x2="102" y2="458"/>
    </g>
    <text class="website" x="114" y="466" font-size="36" textLength="766" lengthAdjust="spacingAndGlyphs">PLDUNMOREELECTRIC.EXAMPLE</text>
  </g>

  <!-- navy footer band with stripes -->
  <g class="footer-band">
    <rect x="0" y="496" width="960" height="224" fill="var(--navy)"/>
    <polygon points="560,679 960,619 960,720 784,720" fill="var(--red)"/>
    <line x1="0" y1="578" x2="800" y2="723" stroke="var(--white)" stroke-width="8"/>
    <text class="slogan" x="84" y="574" font-size="50" textLength="790" lengthAdjust="spacingAndGlyphs">BUILT ON INTEGRITY, DRIVEN BY EXCELLENCE</text>
  </g>
</svg>
</body>
</html>
```